Portfolio site - Need a basic WordPress or SquareSpace site

I need a portfolio site where I have the option to keep updating it on my own. Therefore, I'm guessing I need one that uses WordPress or SquareSpace. I just need a simple and elegant design. I'm a writer (scholarly, fiction and journalism).

Target Market(s)

Adult

Industry/Entity Type

Writer

Number of Pages Required

4 page

Font styles to use
Serif

Colors
b7a5cd
e667a6
85abd2

Requirements
Must have
• Easily updatable features. I'll have to publish links and small blurbs from time to time. And maybe the occasional image.
• Pages should be:
• Home
• Work
• Press
• Contact

```html
<!DOCTYPE html>
<html lang="en">
<head>
<meta charset="utf-8">
<title>Nadira Karim — Writer and Comics Scholar</title>
<link rel="stylesheet" href="https://fonts.googleapis.com/css2?family=Playfair+Display:ital,wght@0,400;0,700;1,400&display=swap">
<style>
  :root {
    --lavender: #b7a5cd;
    --pink: #e667a6;
    --sky: #85abd2;
    --ink: #111111;
    --muted: #6b6b6b;
    --rule: #dcdcdc;
    --chip: #ececec;
    --paper: #ffffff;
  }
  * { margin: 0; padding: 0; box-sizing: border-box; }
  html, body { width: 1200px; height: 675px; overflow: hidden; background: var(--paper); }
  body { font-family: "Playfair Display", Georgia, serif; color: var(--ink); }
  .page { position: relative; width: 1200px; height: 675px; }

  .contact-list { position: absolute; left: 126px; top: 40px; list-style: none; }
  .contact-list li { display: flex; align-items: center; height: 33px; font-style: italic; font-size: 16px; color: var(--muted); }
  .contact-list svg { width: 16px; height: 16px; margin-right: 12px; }

  .brand { position: absolute; left: 0; width: 1200px; top: 48px; text-align: center; }
  .brand-name { font-size: 28px; font-weight: 700; letter-spacing: 0.5px; color: var(--ink); }
  .brand-tagline { font-size: 9px; letter-spacing: 0.5px; color: var(--muted); margin-top: -2px; }

  .social { position: absolute; top: 53px; left: 886px; display: flex; gap: 19px; list-style: none; }
  .social li { width: 38px; height: 38px; border-radius: 50%; background: var(--chip); }
  .social li.is-active { background: var(--sky); }

  .main-nav { position: absolute; left: 0; top: 140px; width: 1200px; height: 51px; border-top: 1px solid var(--rule); border-bottom: 1px solid var(--rule); }
  .main-nav a { position: absolute; top: 14px; transform: translateX(-50%); font-size: 16px; letter-spacing: 3px; color: var(--ink); text-decoration: none; padding: 0 8px 12px; }
  .main-nav a.is-current { color: var(--pink); border-bottom: 3px solid var(--pink); }

  .intro { position: absolute; left: 204px; top: 254px; width: 470px; }
  .drop-cap { position: absolute; left: 0; top: -8px; font-size: 100px; font-style: italic; font-weight: 700; line-height: 1; color: var(--lavender); }
  .intro-text { margin-left: 61px; font-style: italic; font-size: 18.5px; line-height: 30px; letter-spacing: 0.6px; }

  .portrait { position: absolute; left: 744px; top: 251px; width: 252px; height: 252px; border-radius: 50%; background: radial-gradient(circle at 45% 45%, #7a5a4a 0%, #4a3a33 45%, #2d2b2e 100%); }

  .site-footer { position: absolute; left: 0; top: 625px; width: 1200px; height: 50px; border-top: 1px solid var(--rule); font-size: 13px; color: var(--muted); }
  .footer-nav a { position: absolute; top: 17px; color: var(--muted); text-decoration: none; }
  .copyright { position: absolute; right: 123px; top: 17px; }
</style>
</head>
<body>
<div class="page">
  <header>
    <ul class="contact-list">
      <li>
        <svg viewBox="0 0 16 16" aria-hidden="true"><path d="M4 2l2.5 3-1.5 1.5c.8 1.8 2.3 3.3 4.5 4.5L11 9.5l3 2.5-1.5 2C8 14 2 8 2 3.5z" fill="none" stroke="var(--lavender)" stroke-width="1.4" stroke-linejoin="round"/></svg>
        contact@nadirakarim.com
      </li>
      <li>
        <svg viewBox="0 0 16 16" aria-hidden="true"><rect x="1" y="3.5" width="14" height="9" fill="var(--lavender)"/><path d="M1 3.5l7 5 7-5" fill="none" stroke="#fff" stroke-width="1.2"/></svg>
        (555) 200-250-614
      </li>
    </ul>

    <div class="brand">
      <div class="brand-name">Nadira Karim</div>
      <div class="brand-tagline">writer and comics scholar</div>
    </div>

    <ul class="social">
      <li aria-label="Social profile one"></li>
      <li class="is-active" aria-label="Social profile two"></li>
      <li aria-label="Social profile three"></li>
    </ul>
  </header>

  <nav class="main-nav">
    <a class="is-current" href="#" style="left:323px">HOME</a>
    <a href="#" style="left:495px">WORK</a>
    <a href="#" style="left:669px">PRESS</a>
    <a href="#" style="left:861px">CONTACT</a>
  </nav>

  <main>
    <section class="intro">
      <span class="drop-cap">h</span>
      <p class="intro-text">ello my name is Nadira Karim. I am a a writer and comics scholar. She recently published her first short story comic, "1001 Harbourview Nights" in the Harbour Lights Anthology which was illustrated by Lena Morillo. As a comics scholar, her research interests are mainly focused on Muslimah and intersectional superheroes, as well as racialized women in comics.</p>
    </section>
    <div class="portrait" role="img" aria-label="Portrait of the writer holding the anthology in a comic shop"></div>
  </main>

  <footer class="site-footer">
    <nav class="footer-nav">
      <a href="#" style="left:203px">Home</a>
      <a href="#" style="left:278px">Work</a>
      <a href="#" style="left:350px">Press</a>
      <a href="#" style="left:422px">Contact</a>
    </nav>
    <p class="copyright">© Copyright 2018 Nadira Karim. All rights reserved.</p>
  </footer>
</div>
</body>
</html>
```